Business card for auto dealership

Looking for a clean modern design.
Would like attached logo incorporated

Industry/Entity Type

Car dealership

Contact Information for Business Card

Name, website, phone, cell, fax, email

```html
<!DOCTYPE html>
<html lang="en">
<head>
<meta charset="utf-8">
<title>Harlow Truck &amp; Auto Sales — Business Card</title>
<link rel="stylesheet" href="https://fonts.googleapis.com/css2?family=Montserrat:wght@400;600;700&display=swap">
<style>
  :root {
    --backdrop: #4a4a4a;
    --card: #141414;
    --card-back: #1b1b1b;
    --ink: #ffffff;
    --ink-soft: #e6e6e6;
    --emboss: #262626;
  }
  * { margin: 0; padding: 0; box-sizing: border-box; }
  html, body {
    width: 1200px; height: 801px; overflow: hidden;
    background: var(--backdrop);
    font-family: "Montserrat", sans-serif;
  }
  .sheet {
    width: 1200px; height: 801px;
    display: flex; align-items: center; justify-content: center; gap: 40px;
  }
  .card {
    position: relative;
    width: 540px; height: 309px;
    background: var(--card);
    overflow: hidden;
  }
  .card--back { background: var(--card-back); }

  /* front */
  .brand {
    position: absolute; left: 40px; top: 82px;
    color: var(--ink);
    font-weight: 700;
  }
  .brand__name { font-size: 52px; line-height: 1; letter-spacing: 0.5px; }
  .brand__tag { font-size: 13px; letter-spacing: 2.4px; margin-top: 6px; }

  .holder {
    position: absolute; right: 62px; top: 26px;
    text-align: right; color: var(--ink);
  }
  .holder__name { font-size: 19px; font-weight: 700; }
  .holder__role { font-size: 11.5px; font-weight: 400; margin-top: 4px; color: var(--ink-soft); letter-spacing: 0.3px; }
  .edge-tab {
    position: absolute; right: 0; top: 22px;
    width: 40px; height: 18px; background: var(--ink);
  }

  .contacts {
    position: absolute; left: 40px; bottom: 26px;
    list-style: none; color: var(--ink);
    font-size: 13px; line-height: 20px; letter-spacing: 0.4px;
  }
  .contacts li { display: flex; align-items: center; gap: 9px; }
  .contacts svg { width: 12px; height: 12px; fill: var(--ink); flex: none; }

  /* back */
  .back-brand {
    position: absolute; inset: 0;
    display: flex; flex-direction: column; align-items: center; justify-content: center;
    color: var(--emboss); font-weight: 700;
  }
  .back-brand__name { font-size: 76px; line-height: 1; }
  .back-brand__tag { font-size: 18px; letter-spacing: 3.5px; margin-top: 8px; }
</style>
</head>
<body>
<main class="sheet">
  <section class="card card--front">
    <div class="brand">
      <div class="brand__name">Harlow</div>
      <div class="brand__tag">TRUCK &amp; AUTO SALES</div>
    </div>

    <div class="edge-tab"></div>
    <div class="holder">
      <div class="holder__name">Dana Whitfield</div>
      <div class="holder__role">Managing Director</div>
    </div>

    <ul class="contacts">
      <li>
        <svg viewBox="0 0 24 24" aria-hidden="true"><path d="M6.6 10.8a15 15 0 0 0 6.6 6.6l2.2-2.2a1 1 0 0 1 1-.25 11.4 11.4 0 0 0 3.6.6 1 1 0 0 1 1 1V20a1 1 0 0 1-1 1A17 17 0 0 1 3 4a1 1 0 0 1 1-1h3.5a1 1 0 0 1 1 1c0 1.25.2 2.45.6 3.6a1 1 0 0 1-.25 1z"/></svg>
        555-010-4011
      </li>
      <li>
        <svg viewBox="0 0 24 24" aria-hidden="true"><path d="M7 1h10a2 2 0 0 1 2 2v18a2 2 0 0 1-2 2H7a2 2 0 0 1-2-2V3a2 2 0 0 1 2-2zm0 3v14h10V4z"/></svg>
        555-010-2140
      </li>
      <li>
        <svg viewBox="0 0 24 24" aria-hidden="true"><path d="M6 2h10l2 2v5H6zM3 10h18a1 1 0 0 1 1 1v9a1 1 0 0 1-1 1H3a1 1 0 0 1-1-1v-9a1 1 0 0 1 1-1zm4 3v2h10v-2zm0 4v2h10v-2z"/></svg>
        555-010-1774
      </li>
      <li>
        <svg viewBox="0 0 24 24" aria-hidden="true"><path d="M2 5h20v14H2zm2 2v.5l8 5 8-5V7z"/></svg>
        dana@harlowauto.com
      </li>
      <li>
        <svg viewBox="0 0 24 24" aria-hidden="true"><path d="M12 2a10 10 0 1 0 0 20 10 10 0 0 0 0-20zm-1 17.9A8 8 0 0 1 4.1 11H7c.1 3.2.9 6.3 4 8.9zM7 9H4.1A8 8 0 0 1 11 4.1C8 6.7 7.1 8 7 9zm6 10.9c3.1-2.6 3.9-5.7 4-8.9h2.9a8 8 0 0 1-6.9 8.9zM17 9c-.1-1-1-2.3-4-4.9A8 8 0 0 1 19.9 9zM9 11h6c-.1 2.7-1 5-3 6.9-2-1.9-2.9-4.2-3-6.9zm0-2c.2-1.4 1.1-2.8 3-4.7 1.9 1.9 2.8 3.3 3 4.7z"/></svg>
        www.Harlowauto.com
      </li>
    </ul>
  </section>

  <section class="card card--back">
    <div class="back-brand">
      <div class="back-brand__name">Harlow</div>
      <div class="back-brand__tag">TRUCK &amp; AUTO SALES</div>
    </div>
  </section>
</main>
</body>
</html>
```